Zandrix fresh re-design

We are UK based company and have Magento website which we are happy with, but we require fresh design. Menu must be customer friendly

Design must reflect in strength as strength of our products and value for money are our selling points.

Our products are not family products there mainly used for business at events, cycling, running clubs, etc

New design must have same information as current design

links that require new design

http://www.zandrix.example (landing page)

http://www.zandrix.example/3m-x-3m-heavy-duty-tents/3m-x-3m-pop-up-marquee-white.html (product page)

http://www.zandrix.example/custom-design-own-tent-size/choose-3mx3m.html (design tool)

Target Market(s)

business owners, cycling clubs, running clubs,

Industry/Entity Type

It Company

Number of Pages Required

3 page

Requirements
Must have
• background image of working poptent, clean fresh design, printed zandrix eg. cupcake
Should not have
• all same functions as current page

```html
<!DOCTYPE html>
<html lang="en">
<head>
<meta charset="utf-8">
<title>Zandrix – Heavy Duty Pop Up Tents</title>
<link rel="stylesheet" href="https://fonts.googleapis.com/css2?family=Raleway:wght@400;500;600;700;800&family=Open+Sans:wght@400;600;700&display=swap">
<style>
:root{
  --red:#f00a0a;
  --navy:#16237a;
  --blue:#0d2a9c;
  --ink:#2a2a2a;
  --muted:#8a8a8a;
  --line:#e2e2e2;
  --page:#f5f5f5;
  --hero:#e1e1e1;
  --band:#eeeeee;
  --white:#ffffff;
  --dark:#1b1b1b;
  --pink:#f8c6c6;
  --icon:#8c8c8c;
}
*{box-sizing:border-box;margin:0;padding:0}
html,body{width:1200px;height:3237px;overflow:hidden}
body{position:relative;background:var(--page);font-family:"Open Sans",Arial,sans-serif;color:var(--ink)}
.abs{position:absolute}

/* header */
.site-header{left:0;top:0;width:1200px;height:147px;background:#f1f1f1}
.brand{left:56px;top:44px;display:flex;align-items:center;gap:14px;font-family:"Raleway",sans-serif;font-weight:700;font-size:48px;color:var(--navy);letter-spacing:1px}
.brand .mark{width:26px;height:26px;background:var(--red)}
.header-tools{right:50px;top:44px;display:flex;align-items:center;gap:22px}
.search-label{font-size:10px;color:var(--muted);letter-spacing:1px}
.user-box{width:58px;height:58px;background:var(--white);display:flex;align-items:center;justify-content:center;box-shadow:0 1px 3px rgba(0,0,0,.08)}
.cart-count{position:absolute;right:-6px;top:-4px;width:16px;height:16px;border-radius:50%;background:#bbb;color:#fff;font-size:9px;text-align:center;line-height:16px}

/* navigation */
.main-nav{left:0;top:147px;width:1200px;height:80px;background:var(--white);border-bottom:1px solid var(--line)}
.main-nav ul{list-style:none;position:relative;height:100%}
.main-nav li{position:absolute;top:0;height:80px;line-height:80px;font-size:13px;color:#777}
.main-nav li.active{background:var(--red);color:#fff;width:69px;text-align:center;font-weight:600}

/* hero */
.hero{left:0;top:227px;width:1200px;height:621px;background:var(--hero)}
.hero-photo{left:0;top:227px;width:641px;height:496px;background:linear-gradient(160deg,#2149c9 0%,#1a3aa8 45%,#1b1f2e 75%,#2a2f3a 100%)}
.hero-line{left:700px;width:460px;text-align:center;font-family:"Raleway",sans-serif;font-weight:500}
.hero-line.l1,.hero-line.l3{font-size:64px;line-height:68px;color:var(--navy)}
.hero-line.l1{top:318px}
.hero-line.l2{top:395px;font-size:92px;line-height:120px;color:var(--red)}
.hero-line.l3{top:510px}
.btn{display:inline-block;background:var(--red);color:#fff;font-weight:600;text-transform:uppercase;text-align:center}
.hero-btn{left:924px;top:611px;width:194px;height:54px;line-height:54px;font-size:15px}

/* promo cards */
.promo{width:259px;height:222px;top:723px;background:var(--white);text-align:center;box-shadow:0 2px 8px rgba(0,0,0,.12);padding-top:22px}
.promo h3{font-family:"Raleway",sans-serif;font-weight:800;font-size:41px;line-height:41px;color:var(--red);text-transform:uppercase}
.promo p{font-size:13px;color:var(--muted);margin:10px 0 18px}
.promo .btn{width:138px;height:30px;line-height:30px;font-size:10px;border-radius:6px}
.promo.filled{background:var(--red)}
.promo.filled h3,.promo.filled p{color:#fff}
.promo.filled .btn{background:#fff;color:var(--red)}

/* gallery */
.gal-main{left:50px;top:984px;width:684px;height:542px;background:linear-gradient(180deg,#3e4a3a 0%,#1fa889 30%,#1b9778 70%,#6d8a4a 100%)}
.gal-top{left:745px;top:984px;width:410px;height:266px;background:linear-gradient(180deg,#d7d4cc 0%,#cdbf9e 50%,#b5a47d 100%)}
.gal-bottom{left:745px;top:1260px;width:410px;height:266px;background:linear-gradient(180deg,#e0514a 0%,#d9362f 100%)}
.gal-bottom-copy{left:745px;top:1305px;width:410px;text-align:center;font-family:"Raleway",sans-serif;color:#fff;font-size:46px;line-height:54px}
.gal-bottom-btn{left:870px;top:1441px;width:166px;height:50px;line-height:50px;background:#fff;color:var(--red);font-size:12px;text-align:center}

/* products */
.section-title{left:48px;top:1573px;font-family:"Raleway",sans-serif;font-size:22px;font-weight:600;color:var(--red);text-transform:uppercase}
.section-title span{color:var(--navy)}
.sort{left:1060px;top:1570px;width:92px;height:28px;border:1px solid #ccc;background:#fff;font-size:10px;color:#666;padding:7px 8px}
.product{top:1632px;width:254px;height:386px;background:#fff;border:1px solid var(--line);text-align:center}
.product.hover{background:var(--pink)}
.product .tag{position:absolute;left:18px;top:-8px;width:30px;height:14px;background:var(--red);color:#fff;font-size:8px;line-height:14px;font-weight:700}
.product .shot{margin:20px auto 0;width:226px;height:166px}
.product h4{font-size:12px;font-weight:700;margin-top:26px;text-transform:uppercase}
.product p{font-size:9px;color:#999;margin:6px 22px 0;line-height:12px}
.price-row{display:flex;justify-content:center;align-items:center;gap:10px;margin-top:14px}
.old{font-size:11px;color:#aaa;text-decoration:line-through}
.new{font-size:22px;color:var(--red)}
.stars{color:#c00;font-size:14px}
.stars i{font-style:normal;color:#ccc}
.actions{display:flex;justify-content:center;gap:18px;margin-top:14px}
.actions span{width:38px;height:38px;border-radius:50%;border:1px solid #ccc;background:#fff;display:flex;align-items:center;justify-content:center}
.actions span.on{background:var(--red);border-color:var(--red)}
.quick{position:absolute;left:70px;top:80px;width:114px;height:36px;background:rgba(70,70,70,.55);color:#fff;font-size:11px;line-height:36px}

/* latest models */
.models-band{left:0;top:2050px;width:1200px;height:540px;background:var(--band)}
.model{top:2095px;width:357px;height:464px}
.model .panel{position:absolute;left:0;top:167px;width:100%;height:129px;background:var(--red);color:#fff;text-align:center;padding-top:20px}
.model .panel.grey{background:rgba(200,200,200,.85);color:var(--red)}
.model .panel.grey p{color:#333}
.model h3{font-family:"Raleway",sans-serif;font-size:30px;font-weight:500;text-transform:uppercase}
.model p{font-size:11px;line-height:14px;margin-top:8px;padding:0 30px}
.model .btn{position:absolute;left:85px;top:354px;width:170px;height:64px;line-height:64px;font-size:15px;font-weight:700}
.model .btn.blue{background:var(--blue)}

/* features */
.feature{top:2622px;width:259px;height:101px;background:var(--red);color:#fff;display:flex;align-items:center;padding-left:14px}
.feature .ico{width:58px;height:58px;border:2px solid #fff;border-radius:50%;display:flex;align-items:center;justify-content:center;flex:none}
.feature .txt{flex:1;text-align:right;padding-right:16px}
.feature b{display:block;font-size:17px;font-weight:700;text-transform:uppercase}
.feature small{font-size:11px}

/* newsletter */
.news-band{left:0;top:2751px;width:1200px;height:108px;background:#e7e7e7}
.news-input{left:86px;top:2788px;width:364px;height:35px;background:#fff;border:1px solid #ccc;font-size:10px;color:#999;padding:10px 14px}
.news-btn{left:450px;top:2788px;width:78px;height:35px;background:#333;color:#fff;font-size:11px;line-height:35px;text-align:center}
.social{top:2768px;width:74px;height:74px;border-radius:50%;background:#fff;box-shadow:0 2px 6px rgba(0,0,0,.12);display:flex;align-items:center;justify-content:center}
.social.on{background:var(--red)}

/* footer */
.foot-brand{left:106px;top:2960px;font-family:"Raleway",sans-serif;font-weight:700;font-size:32px;color:var(--red)}
.foot-col{top:2890px;width:260px;padding-left:30px;border-left:1px solid var(--line);height:190px}
.foot-col h5{font-family:"Raleway",sans-serif;font-size:17px;font-weight:500;color:#444;margin:10px 0 18px}
.foot-col li{list-style:none;font-size:11px;color:#999;margin-bottom:14px;padding-left:12px;position:relative}
.foot-col li::before{content:"";position:absolute;left:0;top:5px;width:4px;height:4px;border-radius:50%;background:#bbb}
.bottom-bar{left:0;top:3140px;width:1200px;height:97px;background:var(--dark)}
.legal{left:48px;top:3175px;font-size:10px;font-weight:600;color:#fff}
.copy{left:48px;top:3200px;font-size:10px;color:#aaa}
.pay{top:3180px;width:40px;height:26px;border-radius:3px;background:#e9e9e9}
</style>
</head>
<body>

<header class="site-header abs">
  <div class="brand abs"><span class="mark"></span>zandrix</div>
  <div class="header-tools abs">
    <span class="search-label">SEARCH</span>
    <svg width="20" height="20" viewBox="0 0 20 20"><circle cx="8" cy="8" r="6" fill="none" stroke="#f00a0a" stroke-width="3"/><path d="M12.5 12.5 18 18" stroke="#f00a0a" stroke-width="3"/></svg>
    <svg width="20" height="20" viewBox="0 0 20 20"><circle cx="10" cy="10" r="6" fill="none" stroke="#f00a0a" stroke-width="4" stroke-dasharray="3 2"/><circle cx="10" cy="10" r="2.5" fill="#f00a0a"/></svg>
    <span class="user-box"><svg width="18" height="20" viewBox="0 0 18 20"><circle cx="9" cy="5" r="4.5" fill="#f00a0a"/><path d="M0 20c0-6 4-8 9-8s9 2 9 8z" fill="#f00a0a"/></svg></span>
    <span style="position:relative"><svg width="40" height="32" viewBox="0 0 40 32"><path d="M2 4h7l4 18h20l4-13H11" fill="none" stroke="#f00a0a" stroke-width="3"/><circle cx="15" cy="28" r="3" fill="#f00a0a"/><circle cx="30" cy="28" r="3" fill="#f00a0a"/></svg><span class="cart-count">0</span></span>
  </div>
</header>

<nav class="main-nav abs">
  <ul>
    <li class="active" style="left:50px">Home</li>
    <li style="left:160px">Zandrix</li>
    <li style="left:272px">Roofs</li>
    <li style="left:365px">Walls</li>
    <li style="left:455px">Gazebo weights</li>
    <li style="left:613px">Gutters</li>
    <li style="left:714px">Sandbags</li>
    <li style="left:833px">Tables</li>
    <li style="left:928px">Parts</li>
  </ul>
</nav>

<section class="hero abs"></section>
<div class="hero-photo abs" role="img" aria-label="Photo of a blue heavy duty pop up tent with side walls and a clear window"></div>
<div class="hero-line l1 abs">The Stronger</div>
<div class="hero-line l2 abs">Zandrix</div>
<div class="hero-line l3 abs">In the World</div>
<a class="btn hero-btn abs">Shop now</a>

<div class="promo abs" style="left:50px"><h3>Free<br>Gift</h3><p>With order from $ 100</p><span class="btn">Shop now ›</span></div>
<div class="promo abs" style="left:330px"><h3>Get up to<br>20% off</h3><p>Any Single Items</p><span class="btn">Shop now ›</span></div>
<div class="promo abs" style="left:611px"><h3 style="font-size:37px">Gurended<br>100%</h3><p>Keep in you high</p><span class="btn">Shop now ›</span></div>
<div class="promo filled abs" style="left:891px"><h3>Free<br>Shipining</h3><p>on order over $ 99</p><span class="btn">Shop now ›</span></div>

<div class="gal-main abs" role="img" aria-label="Photo of a green pop up tent with walls set up on a lawn"></div>
<div class="gal-top abs" role="img" aria-label="Photo of a beige pop up gazebo with side walls"></div>
<div class="gal-bottom abs" role="img" aria-label="Red tinted photo of a pop up tent on a lawn"></div>
<div class="gal-bottom-copy abs">NEW DUTY<br>POP UP</div>
<a class="gal-bottom-btn abs">READ MORE</a>

<h2 class="section-title abs">Popular <span>Products</span></h2>
<div class="sort abs">SORT BY &nbsp;⌄</div>

<div class="product abs" style="left:54px">
  <span class="tag">25%</span>
  <div class="shot" style="background:linear-gradient(180deg,#4c5a46,#e8e8e8 45%,#5d7a3d)" role="img" aria-label="Photo of a white pop up tent on grass"></div>
  <h4>Name of the product</h4>
  <p>Lorem ipsum dolor sit amet, consectetur adipi scing elit, sed do eiusmod tempor</p>
  <div class="price-row"><span class="old">$35.00</span><span class="new">$ 29.00</span><span class="stars">★★<i>★★</i></span></div>
  <div class="actions">
    <span><svg width="16" height="14" viewBox="0 0 16 14"><path d="M0 1h3l2 8h8l2-6H4" fill="none" stroke="#8c8c8c" stroke-width="1.6"/><circle cx="6" cy="12" r="1.3" fill="#8c8c8c"/><circle cx="12" cy="12" r="1.3" fill="#8c8c8c"/></svg></span>
    <span><svg width="16" height="14" viewBox="0 0 16 14"><path d="M8 13 2 7a3.3 3.3 0 0 1 6-4 3.3 3.3 0 0 1 6 4z" fill="none" stroke="#8c8c8c" stroke-width="1.6"/></svg></span>
    <span><svg width="16" height="16" viewBox="0 0 16 16"><path d="M2 14 14 2M9 2h5v5M2 9v5h5" fill="none" stroke="#8c8c8c" stroke-width="1.6"/></svg></span>
    <span><svg width="16" height="16" viewBox="0 0 16 16"><rect x="1.5" y="1.5" width="13" height="13" fill="none" stroke="#8c8c8c" stroke-width="1.6"/><path d="M4.5 8l2.5 2.5 4.5-5" fill="none" stroke="#8c8c8c" stroke-width="1.6"/></svg></span>
  </div>
</div>
<div class="product hover abs" style="left:334px">
  <span class="tag">25%</span>
  <div class="shot" style="background:linear-gradient(180deg,#f4b8c2,#3a3f9a 50%,#f6c9d0)" role="img" aria-label="Photo of a navy pop up tent with printed branding"></div>
  <span class="quick">QUICK VIEW &nbsp;›</span>
  <h4>Name of the product</h4>
  <p>Lorem ipsum dolor sit amet, consectetur adipi scing elit, sed do eiusmod tempor</p>
  <div class="price-row"><span class="old">$35.00</span><span class="new" style="color:#333">$ 29.00</span><span class="stars">★★<i>★★</i></span></div>
  <div class="actions">
    <span class="on"><svg width="16" height="14" viewBox="0 0 16 14"><path d="M0 1h3l2 8h8l2-6H4" fill="none" stroke="#fff" stroke-width="1.6"/><circle cx="6" cy="12" r="1.3" fill="#fff"/><circle cx="12" cy="12" r="1.3" fill="#fff"/></svg></span>
    <span><svg width="16" height="14" viewBox="0 0 16 14"><path d="M8 13 2 7a3.3 3.3 0 0 1 6-4 3.3 3.3 0 0 1 6 4z" fill="none" stroke="#8c8c8c" stroke-width="1.6"/></svg></span>
    <span><svg width="16" height="16" viewBox="0 0 16 16"><path d="M2 14 14 2M9 2h5v5M2 9v5h5" fill="none" stroke="#8c8c8c" stroke-width="1.6"/></svg></span>
    <span><svg width="16" height="16" viewBox="0 0 16 16"><rect x="1.5" y="1.5" width="13" height="13" fill="none" stroke="#8c8c8c" stroke-width="1.6"/><path d="M4.5 8l2.5 2.5 4.5-5" fill="none" stroke="#8c8c8c" stroke-width="1.6"/></svg></span>
  </div>
</div>
<div class="product abs" style="left:619px">
  <div class="shot" style="background:linear-gradient(180deg,#cfd8de,#d8205a 35%,#5c8a3a 60%)" role="img" aria-label="Photo of a pink pop up tent on a field"></div>
  <h4>Name of the product</h4>
  <p>Lorem ipsum dolor sit amet, consectetur adipi scing elit, sed do eiusmod tempor</p>
  <div class="price-row"><span class="old">$35.00</span><span class="new">$ 29.00</span><span class="stars">★★<i>★★</i></span></div>
  <div class="actions">
    <span><svg width="16" height="14" viewBox="0 0 16 14"><path d="M0 1h3l2 8h8l2-6H4" fill="none" stroke="#8c8c8c" stroke-width="1.6"/><circle cx="6" cy="12" r="1.3" fill="#8c8c8c"/><circle cx="12" cy="12" r="1.3" fill="#8c8c8c"/></svg></span>
    <span><svg width="16" height="14" viewBox="0 0 16 14"><path d="M8 13 2 7a3.3 3.3 0 0 1 6-4 3.3 3.3 0 0 1 6 4z" fill="none" stroke="#8c8c8c" stroke-width="1.6"/></svg></span>
    <span><svg width="16" height="16" viewBox="0 0 16 16"><path d="M2 14 14 2M9 2h5v5M2 9v5h5" fill="none" stroke="#8c8c8c" stroke-width="1.6"/></svg></span>
    <span><svg width="16" height="16" viewBox="0 0 16 16"><rect x="1.5" y="1.5" width="13" height="13" fill="none" stroke="#8c8c8c" stroke-width="1.6"/><path d="M4.5 8l2.5 2.5 4.5-5" fill="none" stroke="#8c8c8c" stroke-width="1.6"/></svg></span>
  </div>
</div>
<div class="product abs" style="left:900px">
  <div class="shot" style="background:linear-gradient(180deg,#d6dde2,#1f4aa8 40%,#5e8a3c 65%)" role="img" aria-label="Photo of a blue pop up tent on a field"></div>
  <h4>Name of the product</h4>
  <p>Lorem ipsum dolor sit amet, consectetur adipi scing elit, sed do eiusmod tempor</p>
  <div class="price-row"><span class="old">$135.00</span><span class="new">$ 129.00</span><span class="stars">★★<i>★★</i></span></div>
  <div class="actions">
    <span><svg width="16" height="14" viewBox="0 0 16 14"><path d="M0 1h3l2 8h8l2-6H4" fill="none" stroke="#8c8c8c" stroke-width="1.6"/><circle cx="6" cy="12" r="1.3" fill="#8c8c8c"/><circle cx="12" cy="12" r="1.3" fill="#8c8c8c"/></svg></span>
    <span><svg width="16" height="14" viewBox="0 0 16 14"><path d="M8 13 2 7a3.3 3.3 0 0 1 6-4 3.3 3.3 0 0 1 6 4z" fill="none" stroke="#8c8c8c" stroke-width="1.6"/></svg></span>
    <span><svg width="16" height="16" viewBox="0 0 16 16"><path d="M2 14 14 2M9 2h5v5M2 9v5h5" fill="none" stroke="#8c8c8c" stroke-width="1.6"/></svg></span>
    <span><svg width="16" height="16" viewBox="0 0 16 16"><rect x="1.5" y="1.5" width="13" height="13" fill="none" stroke="#8c8c8c" stroke-width="1.6"/><path d="M4.5 8l2.5 2.5 4.5-5" fill="none" stroke="#8c8c8c" stroke-width="1.6"/></svg></span>
  </div>
</div>

<section class="models-band abs"></section>
<div class="model abs" style="left:47px;background:linear-gradient(180deg,#dfe3e3,#e9e9e9 30%,#4f7b3a 75%)" role="img" aria-label="Photo of a white pop up tent on grass">
  <div class="panel"><h3>Latest model</h3><p>Lorem ipsum dolor sit amet, consectetur adipiscing elit, sed do eiusmod tempor incididunt</p></div>
  <a class="btn blue">Shop Now</a>
</div>
<div class="model abs" style="left:423px;background:linear-gradient(180deg,#55606a,#2a2f2c 30%,#5b5750 80%)" role="img" aria-label="Photo of a black pop up tent on a patterned court">
  <div class="panel grey"><h3>Latest model</h3><p>Lorem ipsum dolor sit amet, consectetur adipiscing elit, sed do eiusmod tempor incididunt</p></div>
  <a class="btn">Shop Now</a>
</div>
<div class="model abs" style="left:798px;background:linear-gradient(180deg,#3f4a3a,#22b394 25%,#1a8f70 70%,#5e7f3e)" role="img" aria-label="Photo of a green pop up tent with walls">
  <div class="panel"><h3>Latest model</h3><p>Lorem ipsum dolor sit amet, consectetur adipiscing elit, sed do eiusmod tempor incididunt</p></div>
  <a class="btn blue">Shop Now</a>
</div>

<div class="feature abs" style="left:47px"><span class="ico"><svg width="26" height="26" viewBox="0 0 26 26"><path d="M3 11h5v13H3zM10 11l5-9c2 0 3 1 3 3l-1 5h6c1 0 2 1 2 2l-2 10c0 1-1 2-2 2H10z" fill="#fff"/></svg></span><span class="txt"><b>Satisfaction</b><small>100% Guaranteed</small></span></div>
<div class="feature abs" style="left:330px"><span class="ico"><svg width="28" height="22" viewBox="0 0 28 22"><path d="M1 2h16v13H1zM17 6h6l4 5v4H17z" fill="#fff"/><circle cx="6" cy="18" r="3" fill="#fff"/><circle cx="22" cy="18" r="3" fill="#fff"/></svg></span><span class="txt"><b>Free shipping</b><small>on orders over $99</small></span></div>
<div class="feature abs" style="left:611px"><span class="ico"><svg width="26" height="26" viewBox="0 0 26 26"><path d="M21 9a9 9 0 0 0-16 1M5 17a9 9 0 0 0 16-1" fill="none" stroke="#fff" stroke-width="3"/><path d="M22 3v7h-7zM4 23v-7h7z" fill="#fff"/></svg></span><span class="txt"><b>7 day</b><small>Easy to Return items</small></span></div>
<div class="feature abs" style="left:891px"><span class="ico"><svg width="26" height="26" viewBox="0 0 26 26"><circle cx="13" cy="13" r="10" fill="none" stroke="#fff" stroke-width="3"/><circle cx="13" cy="13" r="4" fill="none" stroke="#fff" stroke-width="3"/><path d="M6 6l4 4M20 6l-4 4M6 20l4-4M20 20l-4-4" stroke="#fff" stroke-width="3"/></svg></span><span class="txt"><b>Support</b><small>Customer Service</small></span></div>

<section class="news-band abs"></section>
<div class="news-input abs">Enter Your Email id</div>
<div class="news-btn abs">SIGN UP</div>
<span class="social abs" style="left:815px" aria-label="Social profile"><svg width="22" height="22" viewBox="0 0 22 22"><circle cx="5" cy="11" r="3" fill="#f00a0a"/><circle cx="17" cy="4" r="3" fill="#f00a0a"/><circle cx="17" cy="18" r="3" fill="#f00a0a"/><path d="M5 11 17 4M5 11l12 7" stroke="#f00a0a" stroke-width="2"/></svg></span>
<span class="social on abs" style="left:904px" aria-label="Social profile"><svg width="22" height="22" viewBox="0 0 22 22"><circle cx="5" cy="11" r="3" fill="#fff"/><circle cx="17" cy="4" r="3" fill="#fff"/><circle cx="17" cy="18" r="3" fill="#fff"/><path d="M5 11 17 4M5 11l12 7" stroke="#fff" stroke-width="2"/></svg></span>
<span class="social abs" style="left:990px" aria-label="Social profile"><svg width="22" height="22" viewBox="0 0 22 22"><circle cx="5" cy="11" r="3" fill="#f00a0a"/><circle cx="17" cy="4" r="3" fill="#f00a0a"/><circle cx="17" cy="18" r="3" fill="#f00a0a"/><path d="M5 11 17 4M5 11l12 7" stroke="#f00a0a" stroke-width="2"/></svg></span>
<span class="social abs" style="left:1078px" aria-label="Social profile"><svg width="22" height="22" viewBox="0 0 22 22"><circle cx="5" cy="11" r="3" fill="#f00a0a"/><circle cx="17" cy="4" r="3" fill="#f00a0a"/><circle cx="17" cy="18" r="3" fill="#f00a0a"/><path d="M5 11 17 4M5 11l12 7" stroke="#f00a0a" stroke-width="2"/></svg></span>

<div class="foot-brand abs">Zandrix</div>
<div class="foot-col abs" style="left:369px"><h5>Important Links</h5><ul><li>Affiliate Program</li><li>Special Promotions</li><li>Newsletter</li><li>Contact</li></ul></div>
<div class="foot-col abs" style="left:648px"><h5>Customer Service</h5><ul><li>Contact Us</li><li>Returns</li><li>Site Map</li><li>Forget Password</li></ul></div>
<div class="foot-col abs" style="left:934px;width:230px"><h5>My Account</h5><ul><li>Mey Account</li><li>Order History</li><li>Wish List</li><li>Newsletter</li></ul></div>

<footer class="bottom-bar abs"></footer>
<div class="legal abs">Policies &nbsp;| &nbsp;Privacy &nbsp;| &nbsp;Terms &amp; Conditions</div>
<div class="copy abs">Copyright 2015 Company Name. All Rights Reserved.</div>
<span class="pay abs" style="left:918px" aria-label="Payment method"></span>
<span class="pay abs" style="left:964px" aria-label="Payment method"></span>
<span class="pay abs" style="left:1010px" aria-label="Payment method"></span>
<span class="pay abs" style="left:1056px" aria-label="Payment method"></span>
<span class="pay abs" style="left:1102px" aria-label="Payment method"></span>

</body>
</html>
```